Book Cover for a technology book - The Quiet Lattice

We are writing a book that is a handbook how to build a hybrid cloud - this is a technology concept where companies use cloud services both from the like of Vantrel or Orbisoft and also cloud services built in there own data centers - hence the term hybrid cloud. We want a book cover with the title - The Quiet Lattice; which signifies that we will be teaching companies how to build a hybrid cloud that just works. We want the tagline - handbook for building Hybrid Clouds. The authors are Warren Pelham and Tom Garvey. The cover is to be engaging and feel different than your usual technical manual. I don't have any graphics to help out however will be able to refine and tell you what I don and don't like based on your drafts. The book dimensions are yet to be determined, in the first instance it will be a PDF

Target Market(s)

technology executives and specialists

Industry/Entity Type

Information Technology

Colors

Designer to choose colors to be used in the design.

Requirements
Nice to have
• While I don't have a particular view to how it will look, I'd like the style to be more casual than ultra formal

```html
<!DOCTYPE html>
<html lang="en">
<head>
<meta charset="UTF-8">
<title>The Quiet Lattice — Book Cover</title>
<link href="https://fonts.googleapis.com/css2?family=Exo+2:wght@600;700;800&display=swap" rel="stylesheet">
<style>
  :root {
    --page-bg: #ffffff;
    --cover-blue: #1f5c8b;
    --panel-blue: #286b99;
    --wedge-dark: #2b2d31;
    --title-cyan: #5fd8dc;
    --title-white: #ffffff;
    --tagline-orange: #f7931e;
    --tagline-cyan: #3eeef4;
    --art-light: #6f9cc0;
    --art-dark: #2f3338;
  }
  html, body {
    margin: 0;
    padding: 0;
    width: 1200px;
    height: 1200px;
    overflow: hidden;
    background: var(--page-bg);
  }
  .canvas {
    position: relative;
    width: 1200px;
    height: 1200px;
  }
  .book-cover {
    position: absolute;
    left: 286px;
    top: 115px;
    width: 639px;
    height: 983px;
    background: var(--cover-blue);
    overflow: hidden;
    font-family: "Exo 2", "Trebuchet MS", sans-serif;
  }
  .title-small {
    position: absolute;
    top: 52px;
    left: 0;
    right: 0;
    margin: 0;
    text-align: center;
    font-size: 64px;
    font-weight: 700;
    letter-spacing: 2px;
    line-height: 1;
    color: var(--title-white);
  }
  .title-large {
    position: absolute;
    top: 138px;
    left: 0;
    right: 0;
    margin: 0;
    text-align: center;
    font-size: 120px;
    font-weight: 800;
    letter-spacing: 1px;
    line-height: 1;
    color: var(--title-white);
  }
  .accent { color: var(--title-cyan); }
  .tagline-top {
    position: absolute;
    top: 296px;
    left: 0;
    right: 0;
    text-align: center;
    font-size: 44px;
    font-weight: 700;
    line-height: 1;
    color: var(--title-white);
  }
  .tagline-top .handbook { color: var(--tagline-orange); }
  .tagline-bottom {
    position: absolute;
    top: 355px;
    left: 0;
    right: 0;
    text-align: center;
    font-size: 60px;
    font-weight: 700;
    letter-spacing: 1px;
    line-height: 1;
    color: var(--tagline-cyan);
  }
  .cloud-artwork {
    position: absolute;
    left: 73px;
    top: 459px;
    width: 489px;
    height: 352px;
    border-radius: 170px;
    background: radial-gradient(ellipse at 50% 40%, var(--art-light) 0%, var(--cover-blue) 55%, var(--art-dark) 100%);
    opacity: 0.85;
  }
  .corner-shapes {
    position: absolute;
    inset: 0;
    width: 100%;
    height: 100%;
  }
  .authors {
    position: absolute;
    right: 42px;
    top: 868px;
    text-align: right;
    font-size: 30px;
    font-weight: 700;
    line-height: 37px;
    color: var(--title-white);
  }
</style>
</head>
<body>
<div class="canvas">
  <div class="book-cover">
    <svg class="corner-shapes" viewBox="0 0 490 754" preserveAspectRatio="none" aria-hidden="true">
      <polygon points="100,708 490,590 490,754 165,754" fill="var(--panel-blue)"/>
      <polygon points="39,705 490,586 490,590 100,708 165,754 140,754" fill="var(--wedge-dark)"/>
    </svg>

    <h1 class="title-small"><span class="accent">THE</span> QUIET</h1>
    <p class="title-large"><span class="accent">L</span>ATTICE</p>

    <p class="tagline-top" style="margin:0"><span class="handbook">Handbook for</span> building</p>
    <p class="tagline-bottom" style="margin:0">Hybrid Clouds</p>

    <div class="cloud-artwork" role="img" aria-label="Illustration of a cloud with business people inside, linked by lines to app and device icons such as camera, search, globe, mail, video, document, laptop, shopping cart and phone"></div>

    <div class="authors">
      <div class="author">Warren Pelham</div>
      <div class="author">and Tom Garvey</div>
    </div>
  </div>
</div>
</body>
</html>
```